依頼詳細
11年と長く続いている人気の店ですが、現在店主がワードでメニューを作っていてパッとしないのでリニューアルしたいと考えています。

A4サイズのメニューにしていただきたいです。ページ数は問いません。
完成したものはプリントアウトしてクリアファイルに入れようと考えております。
記載項目
メニューに記載して頂きたい内容は現在のメニューをお渡ししますのでそちらをお使いください。
希望イメージ
シンプル 複雑
単色 カラフル
暗い 明るい
日常 高級
遊び心 厳粛
未来的 伝統的
女性的 男性的
希望する色
黒、赤、濃紺
納品ファイル
• 高解像度JPG (.jpg)
• イラストレーター形式 (.ai)
補足説明
■ 選んだ理由

店主の方と相談させて頂き、スッキリとした分かりやすさと既に全ページ完成されていた点を評価させて頂きました。
修正のご対応、ありがとうございました。

■ 提案者全員のお礼・コメント

ギリギリになってしまい申し訳ございません。
このような低予算の案件にご応募いただき本当にありがとうございました。
始めてのポルテナの利用でしたが、クオリティの高さに驚きました。

今回はプライベートでの利用でしたが、今後は仕事でも使っていきたいと考えておりますので、また何かございましたら一緒にできれば嬉しいです。
宜しくお願い致します。

```html
<!DOCTYPE html>
<html lang="ja">
<head>
<meta charset="utf-8">
<title>焼肉 メニュー</title>
<link rel="stylesheet" href="https://fonts.googleapis.com/css2?family=Shippori+Mincho+B1:wght@600;800&family=Noto+Sans+JP:wght@500;700;900&display=swap">
<style>
  :root {
    --paper: #f1f0ee;
    --paper-shade: #dcdbd8;
    --plum: #5b3a63;
    --ink: #1e1a1a;
    --red: #e2202a;
    --frame: #4a2618;
    --frame-edge: #2f170e;
    --gold: #f4d21c;
    --meat-dark: #7a3b44;
    --meat-light: #c98c8c;
    --leader: #7a7471;
  }
  * { margin: 0; padding: 0; box-sizing: border-box; }
  html, body { width: 846px; height: 1200px; overflow: hidden; }
  body {
    position: relative;
    background: radial-gradient(ellipse at 40% 35%, var(--paper) 0%, #e9e8e5 60%, var(--paper-shade) 100%);
    font-family: "Shippori Mincho B1", serif;
    color: var(--ink);
  }
  .category-mark { position: absolute; left: 0; top: 0; width: 240px; height: 220px; }
  .category-title {
    position: absolute; left: 28px; top: 26px;
    font-family: "Noto Sans JP", sans-serif; font-weight: 900;
    font-size: 50px; color: #fff; letter-spacing: 4px;
  }
  .lead {
    position: absolute; left: 380px; top: 22px;
    font-size: 33px; font-weight: 800; line-height: 1.3; letter-spacing: 2px;
  }
  .lead span { display: block; }
  .lead span + span { padding-left: 72px; }
  .lead-note {
    position: absolute; left: 210px; width: 560px; top: 112px;
    font-family: "Noto Sans JP", sans-serif; font-size: 13px; font-weight: 500;
    text-align: center; color: #3a3434;
  }
  .promo {
    position: absolute; left: 170px; top: 178px;
    font-family: "Noto Sans JP", sans-serif; font-weight: 700;
    font-size: 30px; color: var(--red); letter-spacing: 2px;
  }
  .set-card {
    position: absolute; background: var(--frame);
    border: 3px solid var(--frame-edge);
    box-shadow: 3px 4px 8px rgba(0,0,0,.35);
    padding: 20px 22px 10px;
  }
  .set-card .photo { width: 100%; display: block; }
  .set-card .caption {
    display: flex; align-items: center; justify-content: center; gap: 10px;
    color: #fff; font-weight: 800; margin-top: 8px; line-height: 1.3;
  }
  .set-card .price {
    background: var(--gold); color: var(--red);
    font-family: "Noto Sans JP", sans-serif; font-weight: 900;
    padding: 0 8px; line-height: 1.25;
  }
  .set-card .parts {
    color: #fff; font-family: "Noto Sans JP", sans-serif;
    font-size: 12px; text-align: center; margin-top: 2px; line-height: 1.4;
  }
  .set-all { left: 192px; top: 248px; width: 464px; }
  .set-all .photo { height: 190px; }
  .set-all .caption { font-size: 25px; }
  .set-all .price { font-size: 25px; }
  .set-pork { left: 28px; top: 668px; width: 360px; padding: 16px 18px 8px; }
  .set-pork .photo { height: 160px; }
  .set-pork .caption { font-size: 22px; justify-content: flex-start; }
  .set-pork .price { font-size: 24px; }
  .menu-list { position: absolute; list-style: none; }
  .menu-list li {
    display: flex; align-items: center;
    height: 45px; font-size: 26px; font-weight: 800;
  }
  .list-pork li { height: 46px; }
  .menu-list .name { white-space: nowrap; }
  .menu-list .leader {
    flex: 1; margin: 0 8px;
    border-bottom: 2px dotted var(--leader);
  }
  .menu-list .price {
    font-family: "Noto Sans JP", sans-serif; font-weight: 900; font-size: 25px;
  }
  .menu-list .small { font-size: 20px; }
  .menu-list .badge {
    display: inline-block; width: 22px; height: 22px; border-radius: 50%;
    background: var(--gold); margin-left: 4px; vertical-align: 4px;
  }
  .list-pork { left: 45px; top: 945px; width: 340px; }
  .list-beef { left: 420px; top: 728px; width: 398px; }
</style>
</head>
<body>
  <svg class="category-mark" viewBox="0 0 240 220" aria-hidden="true">
    <path d="M0 0 H205 A115 115 0 0 1 0 190 Z" fill="var(--plum)"/>
  </svg>
  <div class="category-title">焼肉</div>

  <p class="lead"><span>肉本来の旨みを存分に</span><span>味わっていただくために</span></p>
  <p class="lead-note">厳選した食材を丁寧に焼き上げます。新鮮な素材の味わいをご堪能ください。</p>
  <p class="promo">お得な MEGA メニューも大好評！</p>

  <figure class="set-card set-all">
    <div class="photo" role="img" aria-label="皿に盛られたホルモン4種の写真" style="background: radial-gradient(ellipse at 50% 55%, var(--meat-light) 0%, var(--meat-dark) 45%, #1b1212 80%);"></div>
    <figcaption>
      <div class="caption">全ホルモン４種セット<span class="price">790円</span></div>
      <div class="parts">（シロコロ・コブクロ・カシラ・タンシタ）</div>
    </figcaption>
  </figure>

  <figure class="set-card set-pork">
    <div class="photo" role="img" aria-label="皿に盛られた豚ホルモン3種の写真" style="background: linear-gradient(135deg, var(--meat-light) 0%, var(--meat-dark) 55%, #5a2a34 100%);"></div>
    <figcaption>
      <div class="caption">豚ホルモン３種セット<span class="price">590円</span></div>
      <div class="parts">（シロコロ・コブクロ・カシラ）</div>
    </figcaption>
  </figure>

  <ul class="menu-list list-pork">
    <li><span class="name">チョリソー</span><span class="leader"></span><span class="price">390円</span></li>
    <li><span class="name">豚カシラ</span><span class="leader"></span><span class="price">290円</span></li>
    <li><span class="name">豚シロコロ</span><span class="leader"></span><span class="price">290円</span></li>
    <li><span class="name">豚コブクロ</span><span class="leader"></span><span class="price">290円</span></li>
    <li><span class="name">地鶏と玉葱</span><span class="leader"></span><span class="price">390円</span></li>
  </ul>

  <ul class="menu-list list-beef">
    <li><span class="name">上ミノ塩</span><span class="leader"></span><span class="price">490円</span></li>
    <li><span class="name">上ハラミ塩</span><span class="leader"></span><span class="price">490円</span></li>
    <li><span class="name">とにかくタン塩</span><span class="leader"></span><span class="price">390円</span></li>
    <li><span class="name">やっぱり上タン塩</span><span class="leader"></span><span class="price">590円</span></li>
    <li><span class="name">がっつり Mega タン塩</span><span class="leader"></span><span class="price">590円</span></li>
    <li><span class="name"><span class="small">（黒毛和牛）</span>特上タン塩</span><span class="leader"></span><span class="price">890円</span></li>
    <li><span class="name">ゲタカルビ塩</span><span class="leader"></span><span class="price">490円</span></li>
    <li><span class="name">Mega ゲタカルビ塩<span class="badge"></span></span><span class="leader"></span><span class="price">590円</span></li>
    <li><span class="name">Mega カルビ塩</span><span class="leader"></span><span class="price">690円</span></li>
    <li><span class="name">上カルビ塩</span><span class="leader"></span><span class="price">590円</span></li>
  </ul>
</body>
</html>
```